Adventure Business Cards

Please check out our website for style
Vertical card
Details:
Side 1
Logo
Business name: Kestrel Point Wildland Tours
Name: Colin Warbeck
Role: Director
Email: info@kestrelpointtours.com
Address: PO Box 71, Marlin Cove NSW 2471
Phone: +61 2 5550 1847
Web address: www.kestrelpointtours.com
Side 2
Taking pictures?
A Friendwall and Pixlane logo
Tag us in your pictures with
#kpwildtours
@kpwildtours
www.kestrelpointtours.com
Details:
Side 1
Logo
Name: Colin Warbeck
Role: Director
Phone: +61 2 5550 1847
Side 2
Taking pictures?
#kpwildtours
@kpwildtours

```html
<!DOCTYPE html>
<html lang="en">
<head>
<meta charset="utf-8">
<title>Kestrel Point Wildland Tours – Business Cards</title>
<link rel="stylesheet" href="https://fonts.googleapis.com/css2?family=PT+Sans+Narrow:wght@400;700&family=Source+Sans+3:wght@600;700&display=swap">
<style>
  :root {
    --backdrop: #def0fa;
    --navy: #07426e;
    --navy-text: #0b4a79;
    --white: #ffffff;
    --paper: #f6f8fb;
    --grey-text: #5a5f66;
    --map-tint: #eef2f6;
    --shadow: rgba(20, 60, 90, 0.22);
  }
  * { margin: 0; padding: 0; box-sizing: border-box; }
  html, body { width: 1200px; height: 1023px; overflow: hidden; }
  body { background: var(--backdrop); position: relative; font-family: "PT Sans Narrow", sans-serif; }

  .card { position: absolute; top: 197px; width: 358px; height: 626px; box-shadow: 8px 14px 26px var(--shadow); overflow: hidden; }
  .card--front { left: 153px; background: var(--navy); }
  .card--back { left: 677px; background: var(--paper); }

  /* Front */
  .name-band { position: absolute; left: 0; top: 108px; width: 245px; height: 86px; background: var(--white); }
  .name-band::before, .name-band::after { content: ""; position: absolute; left: 0; right: 0; height: 3px; background: var(--navy); }
  .name-band::before { top: 7px; }
  .name-band::after { bottom: 9px; }
  .person-name { position: absolute; left: 37px; top: 20px; font-family: "Source Sans 3", sans-serif; font-weight: 700; font-size: 28px; color: var(--navy-text); line-height: 1; }
  .person-role { position: absolute; left: 39px; top: 52px; font-size: 21px; color: var(--navy-text); line-height: 1; }

  .brand-mark { position: absolute; width: 106px; height: 106px; border-radius: 50%; background: var(--navy); border: 4px solid var(--white);
    display: flex; align-items: center; justify-content: center; text-align: center; padding: 14px;
    font-family: "PT Sans Narrow", sans-serif; font-weight: 700; font-size: 15px; line-height: 1.1; color: var(--white); }
  .card--front .brand-mark { left: 220px; top: 99px; }
  .card--back .brand-mark { left: 215px; top: 484px; width: 112px; height: 112px; border: none; }

  .company-name { position: absolute; left: 37px; top: 231px; font-weight: 700; font-size: 32px; line-height: 35px; color: var(--white); letter-spacing: 0.2px; }

  .contact-list { position: absolute; left: 38px; top: 343px; list-style: none; }
  .contact-list li { display: flex; align-items: center; height: 32px; margin-bottom: 17px; font-size: 18px; color: var(--white); }
  .contact-list li:nth-child(3) { margin-bottom: 18px; }
  .contact-icon { width: 32px; height: 32px; background: var(--white); display: flex; align-items: center; justify-content: center; margin-right: 10px; flex: none; }
  .contact-icon svg { width: 18px; height: 18px; fill: var(--navy); }

  /* Back */
  .island-map { position: absolute; left: 0; top: 0; width: 358px; height: 626px;
    background: radial-gradient(ellipse 48% 40% at 55% 30%, var(--map-tint), transparent 70%); }
  .back-title { position: absolute; left: 45px; top: 140px; font-family: "Source Sans 3", sans-serif; font-weight: 600; font-size: 32px; color: var(--navy-text); line-height: 1; }
  .back-lead { position: absolute; left: 46px; top: 187px; font-size: 21px; color: var(--grey-text); line-height: 1; }
  .social-list { position: absolute; left: 45px; top: 250px; list-style: none; }
  .social-list li { display: flex; align-items: center; height: 50px; margin-bottom: 13px; }
  .social-square { width: 14px; height: 14px; background: var(--navy-text); margin-right: 8px; }
  .social-name { font-size: 19px; color: var(--grey-text); margin-right: 12px; }
  .social-handle { font-size: 26px; color: var(--navy-text); }
  .back-web { position: absolute; left: 45px; top: 383px; font-size: 21px; color: var(--grey-text); line-height: 1; }
</style>
</head>
<body>

<section class="card card--front" aria-label="Business card front">
  <div class="name-band">
    <p class="person-name">Colin Warbeck</p>
    <p class="person-role">Director</p>
  </div>
  <div class="brand-mark">Kestrel Point Wildland Tours</div>

  <h1 class="company-name">Kestrel Point<br>Wildland Tours</h1>

  <ul class="contact-list">
    <li><span class="contact-icon"><svg viewBox="0 0 24 24"><path d="M4 9c0-3 4-5 8-5s8 2 8 5v2h-4V9.5c-1-.6-2.4-1-4-1s-3 .4-4 1V11H4z"/><path d="M7 12l2-2h6l2 2 2 6H5z"/><circle cx="12" cy="15" r="1.8" fill="#fff"/></svg></span>+61 2 5550 1847</li>
    <li><span class="contact-icon"><svg viewBox="0 0 24 24"><path d="M3 6h18v12H3z"/><path d="M3 6l9 7 9-7" fill="none" stroke="#fff" stroke-width="1.6"/></svg></span>info@kestrelpointtours.com</li>
    <li><span class="contact-icon"><svg viewBox="0 0 24 24"><path d="M10 14l4-4M9 11l-3 3a3 3 0 004 4l3-3M15 13l3-3a3 3 0 00-4-4l-3 3" fill="none" stroke="#07426e" stroke-width="2.4" stroke-linecap="round"/></svg></span>www.kestrelpointtours.com</li>
    <li><span class="contact-icon"><svg viewBox="0 0 24 24"><path d="M12 2a7 7 0 00-7 7c0 5 7 13 7 13s7-8 7-13a7 7 0 00-7-7z"/><circle cx="12" cy="9" r="2.6" fill="#fff"/></svg></span>PO Box 71, Marlin Cove NSW 2471</li>
  </ul>
</section>

<section class="card card--back" aria-label="Business card back">
  <div class="island-map" role="img" aria-label="Faint outline map of the island as a background decoration"></div>
  <h2 class="back-title">Taking pictures?</h2>
  <p class="back-lead">Tag us in your pictures with</p>
  <ul class="social-list">
    <li><span class="social-square"></span><span class="social-name">Friendwall</span><span class="social-handle">@kpwildtours</span></li>
    <li><span class="social-square"></span><span class="social-name">Pixlane</span><span class="social-handle">#kpwildtours</span></li>
  </ul>
  <p class="back-web">www.kestrelpointtours.com</p>
  <div class="brand-mark">Kestrel Point Wildland Tours</div>
</section>

</body>
</html>
```